Short-Term Rental Website - Management Services for Property Owner

We are looking for a website to advertise our short-term rental business, Bright Door Stay Management, currently www.brightdoor.ca. Hosted on WordPress.

We have the website main page language but we are looking for someone who is creative and can present the information in a trendy, cool and professional way. I like the closed design crowd job "Plumfield Marketing - SEM, Influencer website. FUN RETRO VIBES" (see attached pictures) in terms of how the page flows, icons and stock images, other connective imagery and design features

Our main competitor website is www.stayvora.com and we like how that website feels but we like the elegance of www.Halvorn-Trask.com (desktop) and main page of www.pombridge.ca (desktop version). We like the slow type video on pombridge.com.

MUST LOOK GOOD ON MOBILE. The mobile experience has to be good.

The content in terms of the language is in one of the attached files.

Our landing page requires the following sections;
- Revenue Maximization
- Services (I have included the content that we want highlighted but we are looking for someone to be creative with how these are displayed
- Pricing
- Featured Properties (display on a carousel) *must design a carousel that can be easily populated.
- Reviews (display on a carousel) *must design a carousel that can be easily populated.
- Contact Us (first name, last name, email, phone (required), description of property)

The header will have;
- Logo (link to main page)
- Pricing (link to pricing section found on the main page)
- Services (link to services section found on the main page)
- Properties (separate page)
- Contact (link to contact area on main page)

We would also need a coded template page that we could use to add additional pages as needed.

For the properties page, we need a landing page that would allow our guests to see all of our properties and a map view with the properties plotted on the map.

As we would collect personal information we would need a cookies/ privacy policy.

The colour palette should be on the light side. We do not want the website to have a dark feel. Colours should be consistent with that of our logo but we are open to creativity.

Target Market(s)

Investment property owners

Industry/Entity Type

Real Estate

Coding

Coded - Design and coding required

Number of Pages Required

2 page

Font styles to use
Sans Serif

Requirements
Must have
• Very strong and well designed landing page

Second page which showcases properttes

Template property page that can be easily reproduced

```html
<!DOCTYPE html>
<html lang="en">
<head>
<meta charset="utf-8">
<title>Bright Door Stay Management</title>
<link href="https://fonts.googleapis.com/css2?family=Poppins:wght@300;400;500;600;700&display=swap" rel="stylesheet">
<style>
:root{
  --teal:#3f8c8c;
  --teal-dark:#2c6a6e;
  --teal-deep:#245a5e;
  --teal-light:#5aa3a1;
  --ink:#2f3b45;
  --muted:#8a949b;
  --line:#dfe5e6;
  --soft:#eef3f3;
  --white:#ffffff;
  --star:#f2b01e;
}
*{box-sizing:border-box;margin:0;padding:0}
html,body{width:1200px;height:4880px;overflow:hidden}
body{font-family:"Poppins",Arial,sans-serif;color:var(--ink);background:var(--white);position:relative}
section,header,footer{position:absolute;left:0;width:1200px}
.abs{position:absolute}
.fill{position:absolute;display:block}

/* Header + hero */
.hero{top:0;height:712px;background:linear-gradient(120deg,#d9d6d1 0%,#efeeea 30%,#c9c6c0 55%,#8d8a86 80%,#6d6a67 100%)}
.hero-photo{inset:0}
.nav{top:0;height:64px;background:rgba(35,45,52,.55);display:flex;align-items:center;padding:0 160px}
.brand{display:flex;align-items:center;gap:10px;color:var(--white);font-weight:600;font-size:22px}
.brand-mark{width:18px;height:18px;background:var(--teal-light);border-radius:3px}
.nav-links{margin-left:auto;display:flex;gap:30px;font-size:12px;color:var(--white);letter-spacing:.5px}
.lang{margin-left:22px;width:38px;height:18px;border-radius:9px;background:var(--teal-dark)}
.hero-panel{right:0;top:520px;width:360px;height:200px;background:rgba(49,125,128,.92);color:var(--white);padding:34px 40px;text-align:right}
.hero-panel p{font-size:18px;line-height:1.45;font-weight:400}
.hero-panel strong{display:block;margin-top:18px;font-size:20px;font-weight:600}
.play{left:30px;top:640px;width:44px;height:44px;border-radius:50%;background:rgba(255,255,255,.85)}

/* Find property */
.find{top:712px;height:228px;background:var(--white)}
.find-block{left:0;top:0;width:620px;height:228px;background:linear-gradient(90deg,var(--teal-dark),var(--teal))}
.find-block h2{position:absolute;left:190px;top:78px;font-size:34px;color:var(--white);font-weight:600}
.find-block span{position:absolute;left:190px;top:128px;font-size:13px;color:#d3e8e7}
.find-form{left:600px;top:36px;width:330px;padding:24px 0 0 0}
.field-label{font-size:12px;color:var(--muted);margin:0 0 6px 2px}
.field{height:36px;border:1px solid var(--line);border-radius:3px;margin-bottom:16px;font-size:12px;color:#b1b8bc;padding:9px 12px;background:var(--white)}
.search-btn{left:946px;top:76px;width:96px;height:96px;background:var(--teal);color:var(--white);font-size:13px;font-weight:500;display:flex;flex-direction:column;align-items:center;justify-content:center;gap:6px}

/* Featured */
.featured{top:940px;height:640px}
.section-title{font-size:28px;font-weight:600;color:var(--ink)}
.section-title em{font-style:normal;color:var(--teal)}
.featured .section-title{position:absolute;left:240px;top:70px}
.featured .sub{position:absolute;left:240px;top:114px;font-size:13px;color:var(--muted)}
.featured .rule{position:absolute;left:240px;top:150px;width:760px;height:1px;background:var(--line)}
.arrow{width:36px;height:36px;border-radius:50%;display:flex;align-items:center;justify-content:center}
.arrow.prev{left:948px;top:142px;background:#e4e9ea}
.arrow.next{left:992px;top:142px;background:var(--teal)}
.card{top:208px;width:232px;height:340px;background:var(--white);box-shadow:0 6px 18px rgba(0,0,0,.08)}
.card .photo{position:absolute;left:0;top:0;width:232px;height:180px}
.card .price{position:absolute;left:14px;top:194px;font-size:17px;font-weight:600}
.card h3{position:absolute;left:14px;top:226px;width:204px;font-size:12px;font-weight:600;line-height:1.45}
.card .rating{position:absolute;left:14px;top:276px;display:flex;gap:3px;color:var(--star);font-size:13px}
.card .rating small{color:var(--muted);font-size:10px;margin-left:14px;margin-top:2px}

/* Services */
.services{top:1580px;height:440px;background:var(--soft)}
.service{top:84px;width:250px;text-align:center}
.service .icon{width:82px;height:82px;border-radius:50%;border:2px solid var(--teal);margin:0 auto 20px;display:flex;align-items:center;justify-content:center;background:var(--white)}
.service h3{font-size:16px;font-weight:500;line-height:1.4;margin-bottom:14px}
.service p{font-size:11px;line-height:1.75;color:var(--muted)}

/* Why */
.why{top:2020px;height:310px}
.why h2{position:absolute;left:240px;top:58px;font-size:30px;font-weight:600}
.why h2 em{font-style:normal;color:var(--teal)}
.why .lead{position:absolute;left:240px;top:112px;font-size:13px;line-height:1.7;color:var(--ink)}
.why .body{position:absolute;left:240px;top:178px;width:470px;font-size:11px;line-height:1.8;color:var(--muted)}
.why .mark{left:870px;top:60px;width:110px;height:110px;border:3px solid #c9d3d4;border-radius:4px}

/* Strip */
.strip{top:2330px;height:340px;display:flex}
.tile{position:relative;width:300px;height:340px}
.tile .tag{position:absolute;bottom:0;left:50%;transform:translateX(-50%);background:var(--white);padding:10px 22px;font-size:12px;font-weight:600;text-align:center;line-height:1.35}
.tile .tag em{font-style:normal;color:var(--teal)}
.tile.safety{background:var(--teal);color:var(--white);padding:40px 30px}
.tile.safety h3{font-size:20px;font-weight:600;margin-bottom:22px}
.tile.safety li{list-style:none;display:flex;gap:10px;font-size:11px;line-height:1.4;margin-bottom:13px}
.tile.safety li span.dot{flex:none;width:9px;height:9px;border-radius:50%;background:var(--white);margin-top:3px}

/* CTA */
.cta{top:2680px;height:140px;background:linear-gradient(90deg,var(--teal-dark),var(--teal-light));display:flex;align-items:center;justify-content:center;gap:40px}
.cta h2{font-size:26px;font-weight:500;color:var(--white)}
.btn-white{background:var(--white);color:var(--teal-dark);font-size:12px;font-weight:600;padding:12px 22px;letter-spacing:.5px}

/* Pricing */
.pricing{top:2820px;height:780px}
.pricing h2{position:absolute;left:0;width:1200px;top:58px;text-align:center;font-size:32px;font-weight:600}
.pricing h2 em{font-style:normal;color:var(--teal)}
.pricing .photo{left:220px;top:150px;width:600px;height:250px}
.price-card{left:660px;top:170px;width:300px;height:410px;background:var(--white);box-shadow:0 10px 30px rgba(0,0,0,.12);text-align:center;padding:34px 26px}
.price-card h3{font-size:18px;font-weight:600;line-height:1.4}
.ring{width:150px;height:150px;border-radius:50%;background:#e7efef;margin:20px auto;display:flex;align-items:center;justify-content:center;font-size:50px;font-weight:500;color:var(--teal)}
.price-card p{font-size:10px;line-height:1.7;color:var(--muted)}
.price-card p u{color:var(--teal)}
.btn-teal{display:inline-block;margin-top:20px;background:var(--teal);color:var(--white);font-size:11px;font-weight:600;padding:12px 18px;letter-spacing:.4px}
.pricing .copy{left:220px;top:430px;width:400px}
.pricing .copy h3{font-size:17px;font-weight:600;line-height:1.45;margin-bottom:22px}
.pricing .copy li{list-style:none;display:flex;gap:14px;font-size:11px;color:var(--muted);line-height:1.6;margin-bottom:14px}
.pricing .copy li .pin{flex:none;width:14px;height:14px;border-radius:50%;background:var(--teal);margin-top:2px}

/* Reviews */
.reviews{top:3600px;height:450px;background:linear-gradient(180deg,#4a5256 0%,#2a3236 60%,#1e2427 100%)}
.reviews .bg{inset:0}
.avatar{left:590px;top:120px;width:130px;height:130px;border-radius:50%;background:linear-gradient(135deg,#d8cfc6,#9b8e84);border:4px solid rgba(255,255,255,.8)}
.quote{left:740px;top:120px;width:330px;color:#eef2f2;font-size:12px;line-height:1.75;font-style:italic}
.quote cite{display:block;margin-top:10px;font-style:normal;color:var(--teal-light);font-size:12px}
.quote cite small{display:block;color:#c7cfd1;font-size:10px}
.dots{left:0;width:1200px;top:400px;display:flex;justify-content:center;gap:8px}
.dots span{width:8px;height:8px;border-radius:50%;background:rgba(255,255,255,.45)}
.dots span.on{background:var(--white)}
.side-arrow{top:200px;width:32px;height:50px;background:var(--teal);display:flex;align-items:center;justify-content:center}

/* Contact */
.contact{top:4050px;height:510px}
.contact h2{position:absolute;left:0;width:1200px;top:60px;text-align:center;font-size:32px;font-weight:600}
.contact h2 em{font-style:normal;color:var(--teal)}
.contact .sub{position:absolute;left:0;width:1200px;top:110px;text-align:center;font-size:13px;color:var(--muted)}
.contact form{position:absolute;left:360px;top:160px;width:480px}
.row{display:flex;gap:20px;margin-bottom:18px}
.input{flex:1;height:38px;border:1px solid var(--line);font-size:11px;color:#aab2b6;padding:11px 12px}
.input.active{border-color:var(--teal)}
.textarea{height:110px;border:1px solid var(--line);font-size:11px;color:#aab2b6;padding:12px}
.send{display:block;margin:26px auto 0;width:120px;height:38px;background:var(--teal);color:var(--white);font-family:inherit;font-size:12px;font-weight:600;border:0;letter-spacing:.5px}

/* Footer */
.footer{top:4560px;height:320px;background:linear-gradient(90deg,var(--teal-deep),var(--teal))}
.footer .brand{position:absolute;left:0;width:1200px;top:60px;justify-content:center;font-size:26px}
.footer .phone{position:absolute;left:0;width:1200px;top:136px;text-align:center;color:var(--white);font-size:32px;font-weight:600}
.footer .mail{position:absolute;left:0;width:1200px;top:186px;text-align:center;color:#d7ebea;font-size:13px}
.footer .links{position:absolute;left:130px;top:142px;font-size:12px;color:var(--white)}
.footer .copy{position:absolute;right:130px;top:142px;font-size:12px;color:var(--white)}
.socials{position:absolute;left:0;width:1200px;top:236px;display:flex;justify-content:center;gap:12px}
.socials span{width:30px;height:30px;border-radius:50%;border:1.5px solid var(--white)}
</style>
</head>
<body>

<header class="hero">
  <div class="fill hero-photo" role="img" aria-label="Bright modern living room with white sofa, red cushions, round rug and dark shelving"></div>
  <nav class="abs nav" style="left:0;width:1200px">
    <div class="brand"><span class="brand-mark"></span>Bright Door</div>
    <div class="nav-links"><span>PRICING</span><span>SERVICES</span><span>PROPERTIES</span><span>CONTACT</span></div>
    <span class="lang"></span>
  </nav>
  <div class="abs hero-panel">
    <p>Your Property's Value will be Optimized to Reach its Potential Through Our Revenue</p>
    <strong>Maximization Services</strong>
  </div>
  <div class="abs play" style="display:flex;align-items:center;justify-content:center">
    <svg width="16" height="16" viewBox="0 0 16 16"><path d="M4 2 L14 8 L4 14 Z" fill="#2c6a6e"/></svg>
  </div>
</header>

<section class="find">
  <div class="abs find-block">
    <h2>Find Property</h2>
    <span>Revenue Maximization</span>
  </div>
  <div class="abs find-form">
    <div class="field-label">When</div>
    <div class="field">Start Date</div>
    <div class="field-label">Guest</div>
    <div class="field">1 Guest</div>
  </div>
  <div class="abs search-btn">
    <svg width="20" height="20" viewBox="0 0 20 20"><circle cx="8" cy="8" r="6" fill="none" stroke="#fff" stroke-width="2"/><path d="M13 13 L18 18" stroke="#fff" stroke-width="2"/></svg>
    SEARCH
  </div>
</section>

<section class="featured">
  <h2 class="section-title">Feature <em>Property</em></h2>
  <p class="sub">Discover New &amp; Upcoming Property</p>
  <div class="rule"></div>
  <div class="abs arrow prev"><svg width="12" height="12" viewBox="0 0 12 12"><path d="M8 2 L4 6 L8 10" fill="none" stroke="#5b666d" stroke-width="1.8"/></svg></div>
  <div class="abs arrow next"><svg width="12" height="12" viewBox="0 0 12 12"><path d="M4 2 L8 6 L4 10" fill="none" stroke="#fff" stroke-width="1.8"/></svg></div>

  <article class="abs card" style="left:240px">
    <div class="photo" role="img" aria-label="Apartment building exterior with balconies" style="background:linear-gradient(160deg,#b9c4cc,#7d8b93)"></div>
    <div class="price">$16007</div>
    <h3>PRIVATE Rooftop in Beautiful East Calm + Parking</h3>
    <div class="rating">★★★★★<small>326 Reviews</small></div>
  </article>
  <article class="abs card" style="left:490px">
    <div class="photo" role="img" aria-label="Wooden terrace with trees and city view" style="background:linear-gradient(160deg,#c8b59b,#7f8c6c)"></div>
    <div class="price">$16299</div>
    <h3>Happiness in The Hills Large Rooms &amp; Green Space</h3>
    <div class="rating">★★★★★<small>1 Reviews</small></div>
  </article>
  <article class="abs card" style="left:740px">
    <div class="photo" role="img" aria-label="Modern bedroom with large bed and window" style="background:linear-gradient(160deg,#e2ddd4,#9f9890)"></div>
    <div class="price">$7419</div>
    <h3>Enchanted Escape - Quiet Private Bedrooms &amp; Yard</h3>
    <div class="rating">★★★★★<small>72 Reviews</small></div>
  </article>
  <article class="abs card" style="left:990px">
    <div class="photo" role="img" aria-label="Bright living room with large windows" style="background:linear-gradient(160deg,#d7dde0,#98a3a8)"></div>
    <div class="price">$7006</div>
    <h3>Fabulous 3Bedroom Condo in an Unbeatable Location</h3>
    <div class="rating">★★★★★<small>54 Reviews</small></div>
  </article>
</section>

<section class="services">
  <div class="abs service" style="left:195px">
    <div class="icon"><svg width="34" height="34" viewBox="0 0 34 34"><circle cx="14" cy="14" r="9" fill="none" stroke="#3f8c8c" stroke-width="2.4"/><path d="M21 21 L30 30" stroke="#3f8c8c" stroke-width="2.6"/></svg></div>
    <h3>Staylist Search Engine Optimization</h3>
    <p>Staylist ranks all listings using an algorithm. We study that algorithm and set each listing to appear higher in search results and attract more bookings.</p>
  </div>
  <div class="abs service" style="left:475px">
    <div class="icon"><svg width="34" height="34" viewBox="0 0 34 34"><path d="M6 26 L6 8 M6 26 L28 26" stroke="#3f8c8c" stroke-width="2.4" fill="none"/><path d="M10 20 L16 14 L20 18 L27 10" stroke="#3f8c8c" stroke-width="2.4" fill="none"/></svg></div>
    <h3>Proprietary Pricing Tool</h3>
    <p>We have developed a proprietary pricing tool that allows us to determine future nightly rates based on demand. This tool has led us to averaging the fifth highest nightly rates in Calgary.</p>
  </div>
  <div class="abs service" style="left:755px">
    <div class="icon"><svg width="34" height="34" viewBox="0 0 34 34"><rect x="5" y="8" width="24" height="20" rx="2" fill="none" stroke="#3f8c8c" stroke-width="2.4"/><path d="M5 14 L29 14 M11 4 L11 10 M23 4 L23 10" stroke="#3f8c8c" stroke-width="2.4"/></svg></div>
    <h3>Strategic Calendar Management</h3>
    <p>Our strategy focuses on future bookings being as long as possible. This, along with other techniques, has resulted in our properties averaging over ninety percent occupancy year round.</p>
  </div>
</section>

<section class="why">
  <h2>Why <em>Bright Door</em></h2>
  <p class="lead">Short-Term Rental Management<br>Integrated, end-to-end rental solutions for residential properties.</p>
  <p class="body">We take care of every detail of your short-term rental, from listing and pricing to cleaning and guest support, so your property earns more while you do less. Our team has built a simple system that keeps owners informed and guests happy every stay.</p>
  <div class="abs mark"></div>
</section>

<section class="strip">
  <div class="tile" role="img" aria-label="Worker installing a ceiling fixture" style="background:linear-gradient(160deg,#d6dfe6,#8ea1ad)">
    <div class="tag">Home <em>Care</em></div>
  </div>
  <div class="tile" role="img" aria-label="Host greeting guests at a doorway" style="background:linear-gradient(160deg,#e8ecef,#a7b1b8)">
    <div class="tag">Guest<br><em>Experience</em></div>
  </div>
  <div class="tile safety">
    <h3>Safety &amp; Security</h3>
    <ul>
      <li><span class="dot"></span>Enter and Comply Compliant</li>
      <li><span class="dot"></span>Delivery Security Window Clean Schedule, and Crime Alert</li>
      <li><span class="dot"></span>Insurance for damage provided by owner</li>
      <li><span class="dot"></span>Unlimited Guest Screening</li>
      <li><span class="dot"></span>Ongoing Guest Risk Assessment</li>
    </ul>
  </div>
  <div class="tile" role="img" aria-label="Professional woman reviewing a report" style="background:linear-gradient(160deg,#ece7e2,#b3a89f)">
    <div class="tag">Performance<br><em>Optimization</em></div>
  </div>
</section>

<section class="cta">
  <h2>Have An Any Question ?</h2>
  <span class="btn-white">GET FREE ESTIMATE</span>
</section>

<section class="pricing">
  <h2>Our <em>Pricing</em></h2>
  <div class="abs photo" role="img" aria-label="Agent showing a document to a smiling couple" style="background:linear-gradient(140deg,#c7d3de,#6f8596)"></div>
  <div class="abs price-card">
    <h3>Bright Door's Share of The Nightly Revenue</h3>
    <div class="ring">20%</div>
    <p>All Money Goes to Your Bank Account, we invoice you once per month.</p>
    <p style="margin-top:8px">There are <u>no additional fees</u> and most of our <u>fee breakdown</u>.</p>
    <span class="btn-teal">CLICK HERE TO SEE EXAMPLE</span>
  </div>
  <div class="abs copy">
    <h3>Our Pricing Structure Is Simple And Easy To Understand, That Is By Design</h3>
    <ul>
      <li><span class="pin"></span>The Nightly Revenue is Split Between the Owner and Bright Door, 80% &amp; 20% Respectively</li>
      <li><span class="pin"></span>The Cleaning fee is paid for by the Guest which Covers All Cleaning Between Guests. We do not Take a Fee From Cleaning</li>
    </ul>
  </div>
</section>

<section class="reviews">
  <div class="fill bg" role="img" aria-label="Modern two-storey house at dusk with lit windows"></div>
  <div class="abs avatar" role="img" aria-label="Portrait of a happy property owner"></div>
  <blockquote class="abs quote">
    “This place has tons of amenities and a great relaxed feel. It was a great size for two couples to share. Weekend having the big patio for drinks in the evenings and the sleep areas felt cozy. We will be back for a night here.”
    <cite>Nina Harlowe, Property Owner<small>January 2019</small></cite>
  </blockquote>
  <div class="abs dots"><span class="on"></span><span></span><span></span><span></span><span></span></div>
  <div class="abs side-arrow" style="left:0"><svg width="10" height="14" viewBox="0 0 10 14"><path d="M7 2 L3 7 L7 12" fill="none" stroke="#fff" stroke-width="2"/></svg></div>
  <div class="abs side-arrow" style="right:0"><svg width="10" height="14" viewBox="0 0 10 14"><path d="M3 2 L7 7 L3 12" fill="none" stroke="#fff" stroke-width="2"/></svg></div>
</section>

<section class="contact">
  <h2>Contact <em>Us</em></h2>
  <p class="sub">Ready to get Started or want more information?</p>
  <form>
    <div class="row"><div class="input active">First Name</div><div class="input">Last Name*</div></div>
    <div class="row"><div class="input">Email Id*</div><div class="input">Phone*</div></div>
    <div class="textarea">Description of Property*</div>
    <button class="send" type="button">SEND US</button>
  </form>
</section>

<footer class="footer">
  <div class="brand"><span class="brand-mark"></span>Bright Door</div>
  <div class="links">Pricing &nbsp;|&nbsp; Services &nbsp;|&nbsp; Properties &nbsp;|&nbsp; Contact</div>
  <div class="phone">403-555-0182</div>
  <div class="mail">info@brightdoor.ca</div>
  <div class="copy">©Bright Door - 2019 All Right Reserved</div>
  <div class="socials"><span></span><span></span></div>
</footer>

</body>
</html>
```